Clean & Inspiring Web Design Project

Larkspur Prototype Studio, LLC (also known as LP-Studio) is a company which provides 3D printing services and products. The emphasis is on making these products and services available to the mass-market - customers and users who may or may not have prior experience with 3D printing and/or rapid prototyping technologies. We are a start-up company, looking to build a clean and creativity inspiring brand - our site must encourage visitor to engage and make something. Our aim is to help take mere ideas and turn them into tangible items. We want to show a fusion of ideas (e.g. pencil sketches on graph paper) with design tools (e.g. CAD and drafting software) and rapid prototyping (e.g. TinkNod 3D printers, Stereolithography Machines, etc.). We would like the website to appear professional but at the same time easy to navigate and a good balance between text and pictures. The final design should inspire customers to nurture their ideas into real products and communicate our services to our customers. Our site should have the feel of a vibrant social community with the added benefit of tangible physical creations.

Target Market(s)

People with great ideas that need to be designed into a real product

Industry/Entity Type

Printing

Requirements
Must have
• - Website design should include 2 layouts - one for a "landing page" and one for a "content page"
- Website design must incorporate attached company logo (or derivative of this logo)
- Website design should incorporate the menu options shown in the attached PDF UI concept (UI does not necessarily need to look like the provided concept, just include all the clickable elements)
- Website design must portray an innovative and cooperative design environment with a look-and-feel that appeals to both amateur and professional designers.
- Please include pictures, illustrations and photographs (as needed) related to 3D printing, CAD design, conventional drafting, engineering and manufacturing industries.
- Design should support scaling to multiple screen sizes, from tablet computers (e.g. Slabix) to very large screen PCs.
- Design should include Username & Password fields for login or a button to pull up a login popup.
Nice to have
• - Website design could include "Invent", "Make", "Produce" and "Buy" options that slowly cycle through - with appropriate photos / graphics. These "menu options" would also be mouse-over enabled to switch into the appropriate context as the cursor enters that region (e.g. mouse over the "Invent" text would bring up page 2, etc.). (See attached Original UI Thoughts)
Should not have
• Requirements - Should Not Have:
- Website design should not portray a service that is very expensive or complicated - we are a reasonably priced service meant to be friendly with amateur inventors
- Website design should not be overly complicated - please keep it reasonably simple
- Website design should not be overly trendy
- Website design should not use more than 2 font styles, gaudy fonts, etc.
- Website design should not be "campy" or "tacky" - playful is ok, but please keep it elegant
- Website design should not be overly masculine or feminine - we will have both women and men as customers

```html
<!DOCTYPE html>
<html lang="en">
<head>
<meta charset="utf-8">
<title>Larkspur Prototype Studio</title>
<link href="https://fonts.googleapis.com/css2?family=Jost:wght@500;600&family=Arimo:wght@400;700&display=swap" rel="stylesheet">
<style>
:root{
  --brand:#17599f;
  --brand-bright:#0aa3ea;
  --brand-deep:#0b5aa2;
  --ink:#111;
  --muted:#555;
  --panel:#f2f2f2;
  --white:#fff;
  --footer:#000;
  --footer-text:#9a9a9a;
  --display:"Jost",sans-serif;
  --body:"Arimo",Arial,sans-serif;
}
*{box-sizing:border-box;margin:0;padding:0}
html,body{width:1200px;height:1100px;overflow:hidden}
body{position:relative;font-family:var(--body);background:var(--white);color:var(--ink)}

.site-header{position:absolute;left:0;top:0;width:1200px;height:108px;background:linear-gradient(#fff,#e9e9e9);border-bottom:1px solid #d4d4d4}
.brand{position:absolute;left:121px;top:10px;display:flex;align-items:center;gap:12px}
.brand-square{width:70px;height:78px;background:var(--brand);border-radius:6px;flex:none}
.brand-name{font-family:var(--display);font-weight:600;font-size:26px;line-height:28px;color:var(--brand);letter-spacing:.3px;white-space:nowrap}
.brand-tagline{display:block;font-family:var(--display);font-weight:500;font-size:12.5px;line-height:16px;color:#222;letter-spacing:.3px}
.top-nav{position:absolute;left:512px;top:50px;display:flex;font-family:var(--display);font-weight:600;font-size:13.5px;letter-spacing:.5px;color:#555;white-space:nowrap}
.top-nav a{color:inherit;text-decoration:none;padding:0 16px;border-left:1px solid #bbb;line-height:16px}
.top-nav a:first-child{border-left:0}
.shop{position:absolute;left:941px;top:42px;width:138px;height:31px;border-radius:5px;background:linear-gradient(#18a4ec,#0a83d3);display:flex;align-items:center;padding-left:10px;color:#fff;font-family:var(--display);font-weight:600;font-size:14px;letter-spacing:.5px;gap:6px}
.shop-count{position:absolute;right:5px;top:5px;width:48px;height:21px;border-radius:4px;background:#fff;color:var(--brand);font-size:16px;line-height:21px;padding-left:10px}
.shop-count::after{content:"";position:absolute;right:6px;top:8px;border:4px solid transparent;border-top-color:#333}

.hero{position:absolute;left:0;top:108px;width:1200px;height:498px;background:linear-gradient(#0c5ba3 0%,#0b7ccc 45%,#09a6ee 100%)}
.main-nav{position:absolute;left:205px;top:0;width:793px;height:52px;clip-path:polygon(0 0,100% 0,95.5% 100%,4.5% 100%);background:linear-gradient(#1ba8ea,#0b8bd8);display:flex;font-family:var(--display);font-weight:600;font-size:16px;letter-spacing:.6px;color:#fff;white-space:nowrap}
.main-nav a{color:inherit;text-decoration:none;display:flex;align-items:center;justify-content:center;height:52px;border-left:1px solid rgba(0,60,120,.35)}
.main-nav a:first-child{border-left:0}
.hero-title{position:absolute;left:121px;top:106px;font-family:var(--display);font-weight:600;font-size:44px;line-height:57.5px;letter-spacing:.5px;color:#fff;white-space:nowrap}
.hero-text{position:absolute;left:121px;top:345px;width:505px;font-size:13.3px;line-height:16.8px;color:#fff}
.hero-frame{position:absolute;left:641px;top:87px;width:430px;height:322px;background:#fff;padding:13px}
.hero-photo{width:404px;height:296px;background:radial-gradient(circle at 70% 45%,#f3f0e6 0%,#c9c6c0 40%,#8f8c86 100%)}
.slide-arrow{position:absolute;top:222px}
.dots{position:absolute;left:557px;top:460px;display:flex;gap:4px}
.dots span{width:14px;height:14px;border-radius:50%;background:#444}
.dots span.active{background:transparent;border:3px solid #fff}

.services{position:absolute;left:0;top:606px;width:1200px;height:342px;background:linear-gradient(#ececec,#fafafa)}
.service-card{position:absolute;top:25px;width:301px;height:281px;background:linear-gradient(#f4f4f4,#fff);border:1px solid #ddd}
.service-card h2{height:32px;background:linear-gradient(#3b3b3b,#000);color:#fff;font-family:var(--display);font-weight:600;font-size:17px;letter-spacing:.6px;text-align:center;line-height:32px;white-space:nowrap;overflow:hidden}
.service-card h2.long{font-size:15px;letter-spacing:.3px}
.service-icon{width:110px;height:110px;margin:18px auto 0;border:4px solid var(--brand-bright);border-radius:50%;background:#fff;padding:6px}
.service-icon div{width:100%;height:100%;border-radius:50%;background:radial-gradient(circle,#e7dcc0,#d8d8d8 70%)}
.service-card h3{margin:22px 0 0 8px;font-size:12px;font-weight:700;letter-spacing:-.15px;white-space:nowrap}
.service-card p{margin:15px 0 0 8px;font-size:12px;line-height:14.5px;letter-spacing:-.2px;color:#222}
.service-card .faded{color:#d4d4d4}

.site-footer{position:absolute;left:0;top:948px;width:1200px;height:152px;background:var(--footer)}
.footer-brand{position:absolute;left:129px;top:19px;display:flex;align-items:center;gap:6px}
.footer-brand .brand-square{width:33px;height:37px;border-radius:3px}
.footer-brand .brand-name{font-size:13px;line-height:14px}
.follow{position:absolute;left:810px;top:26px;display:flex;align-items:center;gap:8px;color:#fff;font-weight:700;font-size:13.5px}
.social{width:26px;height:26px;border-radius:3px;display:block}
.footer-rule{position:absolute;left:127px;width:957px;height:1px;background:#2a2a2a}
.copyright{position:absolute;left:130px;top:92px;font-size:12px;color:var(--footer-text)}
.footer-nav{position:absolute;right:130px;top:92px;font-size:12px;color:var(--footer-text)}
.footer-nav a{color:inherit;text-decoration:none}
</style>
</head>
<body>

<header class="site-header">
  <div class="brand">
    <span class="brand-square"></span>
    <div>
      <div class="brand-name">LARKSPUR<br>PROTOTYPE</div>
      <span class="brand-tagline">What you want ... NOW!</span>
    </div>
  </div>
  <nav class="top-nav">
    <a href="#">WHY LP</a><a href="#">DREAMER</a><a href="#">MAKER</a><a href="#">PRODUCER</a>
  </nav>
  <div class="shop">
    <svg width="20" height="18" viewBox="0 0 20 18" aria-hidden="true"><path d="M1 2h3l3 10h10l2-7H5" fill="none" stroke="#fff" stroke-width="2"/><circle cx="8" cy="15.5" r="1.6" fill="#fff"/><circle cx="16" cy="15.5" r="1.6" fill="#fff"/></svg>
    SHOP
    <span class="shop-count">0</span>
  </div>
</header>

<section class="hero">
  <nav class="main-nav">
    <a href="#" style="width:198px;padding-left:44px">ABOUT LP</a>
    <a href="#" style="width:141px">DREAM</a>
    <a href="#" style="width:128px">MAKE</a>
    <a href="#" style="width:151px">PRODUCE</a>
    <a href="#" style="width:121px">SELL</a>
  </nav>
  <h1 class="hero-title">DREAMING<br>IDEAS<br>FOR<br>INVENEONS</h1>
  <p class="hero-text">Lorem ipsum dolor sit amet, consectetueadipiscing elit, sed diam nonummy nibh euismod tincidunt ut laoreet dolo.Lorem ipsum dolor sit amet, consectetueadipi-scing elit, sed diam nonummy nibh euismod tincidunt ut laoreet dolo.Lorem ipsum dolor sit amet, consectetueadipiscing elit, sed diam nonummy nibh euismod tincid-</p>
  <div class="hero-frame">
    <div class="hero-photo" role="img" aria-label="Photo of light bulbs rising out of an open golden sculpted head"></div>
  </div>
  <svg class="slide-arrow" style="left:60px" width="24" height="40" viewBox="0 0 24 40" aria-label="Previous slide"><path d="M22 1L2 20l20 19" fill="none" stroke="#fff" stroke-width="2"/></svg>
  <svg class="slide-arrow" style="left:1111px" width="24" height="40" viewBox="0 0 24 40" aria-label="Next slide"><path d="M2 1l20 19L2 39" fill="none" stroke="#fff" stroke-width="2"/></svg>
  <div class="dots"><span class="active"></span><span></span><span></span><span></span><span></span></div>
</section>

<section class="services">
  <article class="service-card" style="left:120px">
    <h2>CAD DESIGN</h2>
    <div class="service-icon"><div role="img" aria-label="Illustration of a drafting triangle and pencil on a drawing board"></div></div>
    <h3>Sed ut perspiciatis unde omnis iste natus error sit</h3>
    <p>voluptatem accusantium doloremque laudantiu itotam rem aperiam, eaque ipsa quae ab illo inventorvertatis et quasi architecto beatae vitae dicta sxplicabo. Nemo enim ipsam voluptatem quia voluptas <span class="faded">nihil molestiae<br>sed quia non numquam eius</span></p>
  </article>
  <article class="service-card" style="left:450px">
    <h2>CONVENTIONAL DRAFTING</h2>
    <div class="service-icon"><div role="img" aria-label="Illustration of scissors cutting a drafting sheet"></div></div>
    <h3>Sed ut perspiciatis unde omnis iste natus error sit</h3>
    <p>voluptatem accusantium doloremque laudantiu itotam rem aperiam, eaque ipsa quae ab illo inventorvertatis et quasi architecto beatae vitae dicta sxplicabo. Nemo enim ipsam voluptatem quia voluptas <span class="faded">nihil molestiae<br>sed quia non numquam eius</span></p>
  </article>
  <article class="service-card" style="left:780px">
    <h2 class="long">ENGINEERING &amp; MANUFACTURING</h2>
    <div class="service-icon"><div role="img" aria-label="Illustration of a caliper and protractor"></div></div>
    <h3>Sed ut perspiciatis unde omnis iste natus error sit</h3>
    <p>voluptatem accusantium doloremque laudantiu itotam rem aperiam, eaque ipsa quae ab illo inventorvertatis et quasi architecto beatae vitae dicta sxplicabo. Nemo enim ipsam voluptatem quia voluptas <span class="faded">nihil molestiae<br>sed quia non numquam eius</span></p>
  </article>
</section>

<footer class="site-footer">
  <div class="footer-brand">
    <span class="brand-square"></span>
    <div class="brand-name">LARKSPUR<br>PROTOTYPE</div>
  </div>
  <div class="follow">
    Follow us on:
    <span class="social" style="background:#3b5998" aria-label="Social network one"></span>
    <span class="social" style="background:#2fb7ea" aria-label="Social network two"></span>
    <span class="social" style="background:#c4221f" aria-label="Video channel"></span>
    <svg class="social" width="26" height="26" viewBox="0 0 26 26" aria-label="Email"><rect x="1" y="5" width="24" height="17" fill="#e8e8e8"/><path d="M1 5l12 10L25 5" fill="none" stroke="#aaa" stroke-width="1.5"/></svg>
    <span class="social" style="background:#333" aria-label="Social network three"></span>
  </div>
  <div class="footer-rule" style="top:74px"></div>
  <p class="copyright">© 2012 Larkspur Prototype Studio. All rights reserved.</p>
  <nav class="footer-nav"><a href="#">HOME</a> | <a href="#">CONTACT</a> | <a href="#">FRANCHISE</a> | <a href="#">DISTRIBUTORS</a> | <a href="#">CART</a></nav>
  <div class="footer-rule" style="top:128px"></div>
</footer>

</body>
</html>
```